Letterhead for Law Firm - Logo already prepared

I previously used to prepare a logo which I was quite pleased with, a copy is attached for your reference. I would like the font of the logo to be all the same size, rather than the 'S' and 'L' being larger than the other letters.
I have copies of the attached in other formats if necessary.
I need a letterhead prepared which is virtually identical to the draft attached, however I will be adding an address, phone number, fax number, mobile number and email. I will provide these details with whoever can assist me.
I will also be providing insurance details to be listed at the foot of the page.
Finally, I need the file to be supplied as a high resolution pdf with 2mm bleed.
If you require any further information, please do not hesitate to contact me.

```html
<!DOCTYPE html>
<html lang="en">
<head>
<meta charset="utf-8">
<title>Marlowe Legal – Letterhead</title>
<link href="https://fonts.googleapis.com/css2?family=Mulish:wght@600;700&display=swap" rel="stylesheet">
<style>
  :root {
    --paper: #ffffff;
    --ink: #3a3a3a;
    --rule: #b5b5b5;
    --orange: #f7941d;
    --orange-deep: #f15a24;
    --orange-light: #fbb040;
    --halftone: #ececec;
  }
  html, body {
    margin: 0;
    padding: 0;
    overflow: hidden;
    background: var(--paper);
  }
  .letterhead {
    position: relative;
    width: 906px;
    height: 1200px;
    overflow: hidden;
    background: var(--paper);
    font-family: "Mulish", "Century Gothic", sans-serif;
  }
  .brand {
    position: absolute;
    top: 17px;
    right: 16px;
    display: flex;
    align-items: center;
    gap: 12px;
  }
  .brand-dot {
    width: 66px;
    height: 66px;
    border-radius: 50%;
    background: var(--orange);
  }
  .brand-name {
    font-weight: 600;
    font-size: 31px;
    letter-spacing: 1px;
    text-transform: uppercase;
    color: var(--ink);
  }
  .header-rule {
    position: absolute;
    left: 0;
    top: 101px;
    width: 100%;
    height: 2px;
    background: var(--rule);
    box-shadow: 0 4px 0 #d6d6d6;
  }
  .halftone-field {
    position: absolute;
    left: -120px;
    top: 110px;
    width: 760px;
    height: 960px;
    background: radial-gradient(ellipse at 25% 45%, var(--halftone) 0%, rgba(236,236,236,0.5) 35%, rgba(255,255,255,0) 70%);
  }
  .footer-wave {
    position: absolute;
    left: 0;
    top: 0;
    width: 906px;
    height: 1200px;
  }
  .footer-contact {
    position: absolute;
    bottom: 18px;
    left: 18px;
    right: 20px;
    display: flex;
    justify-content: space-between;
    font-weight: 700;
    font-size: 17px;
    color: var(--paper);
  }
</style>
</head>
<body>
  <main class="letterhead">
    <div class="halftone-field" role="img" aria-label="Soft grey halftone dot pattern fading across the page"></div>

    <header class="brand">
      <span class="brand-dot"></span>
      <span class="brand-name">Marlowe Legal</span>
    </header>
    <div class="header-rule"></div>

    <svg class="footer-wave" viewBox="0 0 906 1200" aria-hidden="true">
      <defs>
        <linearGradient id="footerFill" x1="0" y1="0" x2="0" y2="1">
          <stop offset="0" stop-color="#f7941d"/>
          <stop offset="1" stop-color="#f15a24"/>
        </linearGradient>
      </defs>
      <path d="M0,1116 C360,1138 700,1100 906,1010 L906,1200 L0,1200 Z" fill="#fbb040"/>
      <path d="M0,1124 C360,1146 700,1112 906,1020 L906,1200 L0,1200 Z" fill="url(#footerFill)"/>
    </svg>

    <footer class="footer-contact">
      <span class="footer-phone-web">Ph ; 000-000-0000 I www.websitelinkhere.com</span>
      <span class="footer-address">Address line here 1, Address line here 1</span>
    </footer>
  </main>
</body>
</html>
```